Oil & Gas Energy Consultancy Service

I am an experienced Upper Management former employed by a Global Service Company to the Oil & Gas Industry.
After 22 years I have decided to go as a Consultant working mainly in the same,(upper management) areas of work.
This is a, "One Man" operation.
Updates

Thank you all for your interest and professionalism in this little project.

It was hard to decide on a final contestant but it had to come down to one selection.
Best of luck with your other work & projects!
Tavo Ressani-Merrick

Industry/Entity Type

Industry

Contact Information for Business Card

Trelumo Energy Services, Inc
Tavo Ressani-Merrick - Managing Director
O&G Consultants
Suite 4140, Tower 3, Halden Ave, Edmonton, AB, T6K 2P5 Canada
250 555 0194 tavo.merrick@trelumo-example.net

Logo Text

Trelumo Energy Services

Logo styles of interest
Abstract Logo

```html
<!DOCTYPE html>
<html lang="en">
<head>
<meta charset="utf-8">
<title>Trelumo Energy Services – Business Card</title>
<link href="https://fonts.googleapis.com/css2?family=Play:wght@700&family=PT+Sans+Narrow:wght@400&display=swap" rel="stylesheet">
<style>
  :root {
    --page: #e7e4e0;
    --card-light: #ffffff;
    --card-light-edge: #e4e5e7;
    --card-dark: #3b3531;
    --card-dark-edge: #2c2724;
    --ink: #2f2a27;
    --ink-soft: #3d3835;
    --orange: #e27125;
    --silver: #d9d9d9;
  }
  html, body {
    margin: 0;
    padding: 0;
    width: 1200px;
    height: 1108px;
    overflow: hidden;
    background: var(--page);
  }
  .canvas {
    position: relative;
    width: 1200px;
    height: 1108px;
  }
  .card {
    position: absolute;
    left: 262px;
    width: 676px;
    height: 368px;
    overflow: hidden;
    box-shadow: 0 6px 14px rgba(0,0,0,.25);
  }
  .card--front {
    top: 171px;
    background: radial-gradient(ellipse at 30% 35%, var(--card-light) 0%, var(--card-light) 35%, var(--card-light-edge) 100%);
  }
  .card--back {
    top: 567px;
    background: radial-gradient(ellipse at 50% 30%, #4a423d 0%, var(--card-dark) 45%, var(--card-dark-edge) 100%);
  }
  .brand {
    position: absolute;
    display: flex;
    align-items: center;
    font-family: "Play", sans-serif;
    font-weight: 700;
    font-size: 29px;
    letter-spacing: 0.2px;
    white-space: nowrap;
  }
  .brand__dot {
    width: 22px;
    height: 22px;
    border-radius: 50%;
    background: var(--orange);
    margin-right: 14px;
    flex: none;
  }
  .card--front .brand {
    left: 130px;
    top: 52px;
    color: var(--ink);
  }
  .card--back .brand {
    left: 0;
    right: 0;
    top: 90px;
    flex-direction: column;
    color: var(--silver);
  }
  .card--back .brand__dot {
    margin: 0 0 18px 0;
  }
  .person {
    position: absolute;
    left: 93px;
    top: 182px;
    width: 210px;
    text-align: center;
  }
  .person__name {
    font-family: "Play", sans-serif;
    font-weight: 700;
    font-size: 24px;
    color: var(--ink-soft);
    padding-bottom: 2px;
    border-bottom: 2px solid var(--orange);
    white-space: nowrap;
  }
  .person__role {
    font-family: "PT Sans Narrow", sans-serif;
    font-size: 17px;
    color: var(--ink);
    margin-top: 3px;
  }
  .contact {
    position: absolute;
    left: 397px;
    top: 186px;
    margin: 0;
    padding: 0;
    list-style: none;
    font-family: "PT Sans Narrow", sans-serif;
    font-size: 17px;
    line-height: 24px;
    color: var(--ink);
  }
  .contact__item {
    display: flex;
    align-items: flex-start;
  }
  .contact__icon {
    width: 16px;
    height: 16px;
    margin: 4px 8px 0 0;
    flex: none;
    fill: var(--ink);
  }
  .band {
    position: absolute;
    left: 0;
    bottom: 0;
    width: 676px;
    height: 33px;
  }
</style>
</head>
<body>
<main class="canvas">

  <section class="card card--front" aria-label="Business card front">
    <div class="brand">
      <span class="brand__dot"></span>
      <span class="brand__name">Trelumo Energy Services, Inc</span>
    </div>

    <div class="person">
      <div class="person__name">Tavo Ressani-Merrick</div>
      <div class="person__role">O&amp;G Consultants</div>
    </div>

    <ul class="contact">
      <li class="contact__item">
        <svg class="contact__icon" viewBox="0 0 16 16" aria-hidden="true"><rect x="4" y="1" width="8" height="14" rx="1.5"/><rect x="5.5" y="3" width="5" height="5" fill="#fff"/></svg>
        <span>250 555 0194</span>
      </li>
      <li class="contact__item">
        <svg class="contact__icon" viewBox="0 0 16 16" aria-hidden="true"><path d="M8 1 L1 8 H3 V15 H7 V10 H9 V15 H13 V8 H15 Z"/></svg>
        <span>Suite 4140, Tower 3<br>Halden Ave, Edmonton<br>AB, T6K 2P5 Canada</span>
      </li>
      <li class="contact__item">
        <svg class="contact__icon" viewBox="0 0 16 16" aria-hidden="true"><path d="M1 3 H15 V13 H1 Z M2.5 4.5 V11.5 H13.5 V4.5 L8 9 Z M3 4.2 L8 8 L13 4.2 Z" fill-rule="evenodd"/></svg>
        <span>tavo.merrick@trelumo-example.net</span>
      </li>
    </ul>

    <svg class="band" viewBox="0 0 676 33" preserveAspectRatio="none" aria-hidden="true">
      <polygon points="198,1 286,1 274,33 190,33" fill="var(--ink)"/>
      <polygon points="296,1 676,1 676,33 284,33" fill="var(--orange)"/>
    </svg>
  </section>

  <section class="card card--back" aria-label="Business card back">
    <div class="brand">
      <span class="brand__dot"></span>
      <span class="brand__name">Trelumo Energy Services, Inc</span>
    </div>

    <svg class="band" viewBox="0 0 676 33" preserveAspectRatio="none" aria-hidden="true">
      <polygon points="59,0 676,0 676,33 45,33" fill="var(--orange)"/>
    </svg>
  </section>

</main>
</body>
</html>
```